依頼詳細
■ラベルデザインへの要望

いわゆる機能性表示食品の他商品のように
すこし権威性のある固めのデザインにしたい。
イラストは入れらませんが、【筋肉】と【睡眠】をイメージできるデザインを希望します。
逆にいうと筋肉と睡眠をイメージできれば色はデザイナー様にお任せします。
メインターゲットは50代以上の男女ですが、高齢者向けになりすぎないようにお願いいたします。

【表面】

★下記文言を入れたい
・届出表示
・本品は、事業者の責任において特定の保険の目的が期待できる旨を表示するものとして、購買民局長官に届出されたものです。ただし、特定保健用食品と異なり、購買民局長官による個別の審査を受けたものではありません。
・機能性表示食品
・1日1粒目安/31日分
・食生活は、主食、主菜、副菜を基本に、食事のバランスを。

★添付の「青嶺ナチュラ」のロゴも入れたい

【裏面】
表面が確定したのち別途ご依頼します。

■想定ターゲット:50歳以上 男女

その他何かご不明な点がございましたら、お気軽にご質問下さい。
よろしくお願いいたします。
記載項目
■ラベルの情報

アルミパウチ デジタル印刷

ラベルサイズ
縦 160mm
横 100mm
希望イメージ
シンプル 複雑
単色 カラフル
暗い 明るい
日常 高級
遊び心 厳粛
未来的 伝統的
女性的 男性的
希望する色
納品ファイル
補足説明
■ 選んだ理由

片方の訴求に偏りすぎずデザインしていただいた点を評価しております。

■ 提案者全員のお礼・コメント

この度は弊社コンペにご参加いただきまして誠にありがとうございました。
今後も開催予定ですので、またご機会あれば奮ってご参加ください。

```html
<!DOCTYPE html>
<html lang="ja">
<head>
<meta charset="UTF-8">
<title>私のまいにち習慣 ラベル</title>
<link href="https://fonts.googleapis.com/css2?family=Noto+Sans+JP:wght@400;500;700&family=Roboto:wght@400;500&display=swap" rel="stylesheet">
<style>
  :root {
    --bg: #e6e7e9;
    --label-top: #ffffff;
    --label-bottom: #eef0f2;
    --blue: #1f7fc4;
    --blue-dark: #15609a;
    --ink: #333a40;
    --muted: #7b8288;
    --rule: #c9cdd1;
    --notice-bg: #f3f4f5;
  }
  * { margin: 0; padding: 0; box-sizing: border-box; }
  html, body { width: 849px; height: 1200px; overflow: hidden; }
  body {
    background: var(--bg);
    font-family: "Noto Sans JP", sans-serif;
    color: var(--ink);
    position: relative;
  }
  .label {
    position: absolute;
    left: 124px; top: 120px;
    width: 600px; height: 960px;
    background: linear-gradient(180deg, var(--label-top), var(--label-bottom));
    box-shadow: 0 2px 10px rgba(0,0,0,0.12);
  }
  .side-band {
    position: absolute;
    left: 30px; top: 120px;
    width: 52px; height: 500px;
    background: var(--blue);
  }
  .side-band span {
    position: absolute;
    left: 50%; top: 50%;
    transform: translate(-50%, -50%) rotate(-90deg);
    font-family: "Roboto", sans-serif;
    font-size: 38px;
    letter-spacing: 1px;
    color: #fff;
    white-space: nowrap;
  }
  .top-rule {
    position: absolute;
    left: 82px; top: 120px;
    width: 518px; height: 3px;
    background: var(--blue);
  }
  .category {
    position: absolute;
    left: 104px; top: 146px;
    padding: 4px 12px;
    border: 1px solid var(--muted);
    font-size: 15px;
    color: var(--ink);
  }
  .product-name {
    position: absolute;
    left: 104px; top: 196px;
    font-size: 46px;
    font-weight: 500;
    color: var(--blue);
    letter-spacing: 1px;
  }
  .title-rule {
    position: absolute;
    left: 82px; top: 270px;
    width: 518px; height: 7px;
    background: var(--blue);
  }
  .code {
    position: absolute;
    left: 104px; top: 282px;
    font-family: "Roboto", sans-serif;
    font-size: 16px;
    color: var(--blue-dark);
  }
  .claim {
    position: absolute;
    left: 104px; top: 330px;
    width: 460px;
    font-size: 14.5px;
    line-height: 1.85;
    color: var(--ink);
  }
  .dosage-badge {
    position: absolute;
    left: 474px; top: 520px;
    width: 96px; height: 74px;
    border: 2px solid var(--blue);
    background: #fff;
    text-align: center;
  }
  .dosage-badge .dose {
    display: block;
    background: var(--blue);
    color: #fff;
    font-size: 14px;
    font-weight: 700;
    padding: 5px 0;
  }
  .dosage-badge .days {
    display: block;
    font-size: 18px;
    font-weight: 700;
    color: var(--blue);
    padding-top: 8px;
  }
  .diet-note {
    position: absolute;
    left: 104px; top: 540px;
    width: 350px;
    font-size: 12px;
    line-height: 1.8;
    color: var(--muted);
  }
  .notice {
    position: absolute;
    left: 30px; top: 650px;
    width: 540px;
    padding: 16px 20px;
    background: var(--notice-bg);
    border-top: 1px solid var(--rule);
    border-bottom: 1px solid var(--rule);
    font-size: 12px;
    line-height: 1.8;
    color: var(--muted);
  }
  .notice h2 {
    font-size: 13px;
    font-weight: 700;
    color: var(--ink);
    margin-bottom: 4px;
  }
  .brand {
    position: absolute;
    left: 0; right: 0; top: 820px;
    display: flex;
    justify-content: center;
    align-items: center;
    gap: 12px;
  }
  .brand-mark {
    width: 26px; height: 26px;
    background: var(--blue);
  }
  .brand-name {
    font-size: 22px;
    font-weight: 500;
    color: var(--ink);
    letter-spacing: 2px;
  }
</style>
</head>
<body>
  <section class="label">
    <div class="side-band"><span>Supplement</span></div>
    <div class="top-rule"></div>
    <div class="category">機能性表示食品</div>
    <h1 class="product-name">私のまいにち習慣</h1>
    <div class="title-rule"></div>
    <div class="code">KR-07</div>
    <p class="claim">
      本品にはGABAが含まれます。<br>
      GABAには日常の歩行活動により、中高年の方の加齢に伴い低下する筋肉量を維持する機能が報告されています。<br>
      また、GABAには睡眠の質（眠りの深さ、すっきりとした目覚め）の改善に役立つことが報告されています。
    </p>
    <p class="diet-note">食生活は、主食、主菜、副菜を基本に、食事のバランスを。</p>
    <div class="dosage-badge">
      <span class="dose">1日1粒目安</span>
      <span class="days">31日分</span>
    </div>
    <div class="notice">
      <h2>届出表示</h2>
      本品は、事業者の責任において特定の保険の目的が期待できる旨を表示するものとして、購買民局長官に届出されたものです。ただし、特定保健用食品と異なり、購買民局長官による個別の審査を受けたものではありません。
    </div>
    <div class="brand">
      <div class="brand-mark"></div>
      <span class="brand-name">青嶺ナチュラ</span>
    </div>
  </section>
</body>
</html>
```